Postcard for Funeral Homes

We need a double-sided postcard 8.5" x 5.5" to be sent to the Directors of Funeral Homes advising them of our White Dove Releases for funerals and memorial services. This is a business to business marketing piece that we are using to introduce Lantern Glow Tributes services to Funeral Homes.

Lantern Glow Tributes is the originator of White Dove Releases in the Greater Toronto Area. A professional White Dove Release is a beautiful tribute to the lives of those who are no longer with us, expressing peace for the one who has moved on and comfort for those who remain. Releasing the White Doves and watching as they soar upwards to the heavens provides a spiritually uplifting moment during a time of grief.

A single White Dove is released first, representing the spirit of the deceased transcending from one state to another. The single Dove is followed by a flock of White Doves, nestled in and released from special white latticework pillars.

We want to communicate that White Dove Releases should be included in the options available through the Funeral Homes when arrangements are being made by the family of the deceased.

The design should convey professionalism and dependability in addition to being graceful, beautiful and spiritually comforting (without any reference to a particular religion). For more information what Lantern Glow Tributes offers, please visit www.lanternglowtributes.com

Target Market(s)

We are targeting the Directors of Funeral Homes and Cemeteries who make decisions on what services and arrangements to offer the families of the deceased.

Requirements
Must have
• The design must have space for us to affix mailing labels and a stamp.
• There should be Images of White Doves and dove releases at cemeteries.
• Text for the front and back of the postcard has been provided.
Should not have
• There cannot be any religious images or specific religious symbols

```html
<!DOCTYPE html>
<html lang="en">
<head>
<meta charset="utf-8">
<title>Lantern Glow Tributes – Postcard Back</title>
<link rel="stylesheet" href="https://fonts.googleapis.com/css2?family=EB+Garamond:ital@1&family=Libre+Caslon+Text:wght@700&family=Montserrat:wght@600&display=swap">
<style>
  :root {
    --ink: #1d1d1d;
    --paper: #ffffff;
    --rule: #222222;
    --sky-deep: #6e9bd8;
    --sky-mid: #9cc0ea;
    --sky-light: #d7e7f7;
    --url-grey: #c9c9c9;
  }
  * { margin: 0; padding: 0; box-sizing: border-box; }
  html, body { width: 1200px; height: 777px; overflow: hidden; background: var(--paper); }
  .postcard {
    position: relative;
    width: 1200px;
    height: 777px;
    background: var(--paper);
    border: 1px solid #555;
    color: var(--ink);
  }
  .message-side { position: absolute; left: 0; top: 0; width: 522px; height: 100%; }
  .intro {
    position: absolute;
    left: 53px;
    top: 46px;
    width: 430px;
    font-family: "Libre Caslon Text", Georgia, serif;
    font-weight: 700;
    font-size: 16.4px;
    line-height: 23.6px;
  }
  .benefits {
    position: absolute;
    left: 53px;
    top: 226px;
    width: 450px;
    list-style: none;
    font-family: "EB Garamond", Garamond, serif;
    font-style: italic;
    font-size: 20.5px;
    line-height: 26px;
  }
  .benefits li { position: relative; padding-left: 18px; }
  .benefits li::before {
    content: "";
    position: absolute;
    left: 2px;
    top: 10px;
    width: 7px;
    height: 7px;
    border-radius: 50%;
    background: var(--ink);
  }
  .contact-panel {
    position: absolute;
    left: 43px;
    top: 459px;
    width: 453px;
    height: 215px;
    background:
      radial-gradient(ellipse 55% 80% at 82% 55%, #ffffff 0%, #f2f4f7 35%, rgba(255,255,255,0) 70%),
      linear-gradient(180deg, var(--sky-deep) 0%, var(--sky-mid) 60%, var(--sky-light) 100%);
  }
  .contact-call {
    position: absolute;
    left: 32px;
    top: 25px;
    font-family: "Montserrat", Arial, sans-serif;
    font-weight: 600;
    font-size: 17px;
    line-height: 21.6px;
    color: var(--ink);
  }
  .contact-phone {
    position: absolute;
    left: 32px;
    top: 158px;
    font-family: "Libre Caslon Text", Georgia, serif;
    font-weight: 700;
    font-size: 31px;
    letter-spacing: 0.5px;
    color: var(--ink);
  }
  .web-address {
    position: absolute;
    left: 53px;
    top: 688px;
    font-family: "Libre Caslon Text", Georgia, serif;
    font-weight: 700;
    font-size: 32px;
    color: var(--url-grey);
    letter-spacing: -0.5px;
  }
  .divider {
    position: absolute;
    left: 521px;
    top: 50px;
    width: 2px;
    height: 678px;
    background: var(--rule);
  }
  .address-side { position: absolute; left: 523px; top: 0; right: 0; height: 100%; }
</style>
</head>
<body>
  <main class="postcard">
    <section class="message-side">
      <p class="intro">A professional White Dove Release is a beautiful tribute to the lives of those who are no longer with us, expressing peace for the one who has moved on and comfort for those who remain. Releasing the White Doves and watching as they soar upwards to the heavens provides a spiritually uplifting moment during a time of grief.</p>
      <ul class="benefits">
        <li>Spiritual complement to burial, cremation,<br>and memorial services</li>
        <li>Symbolizes the spirit transcending from<br>one state to another</li>
        <li>Non-denominational, multi-cultural</li>
        <li>Appropriate for traditional and non-traditional services</li>
        <li>Poems and readings available</li>
        <li>Professional, dependable and respectful staff</li>
      </ul>
      <div class="contact-panel" role="img" aria-label="Photo of a white dove with spread wings against a soft blue sky">
        <p class="contact-call">Contact us today<br>for information on<br>how to include a<br>White Dove Release<br>as part of your<br>special event!</p>
        <p class="contact-phone">416.555.0148</p>
      </div>
      <p class="web-address">lanternglowtributes.com</p>
    </section>
    <div class="divider"></div>
    <section class="address-side" aria-label="Mailing label and stamp area"></section>
  </main>
</body>
</html>
```